Email Signature

We are looking for creative email signature for our company. Please find attached the logo of our company for your reference. now we understand there isn't much can be done with email signature but we are looking for out of the box designs. Nothing specific in mind

Please insert fake numbers, website and/or address, etc just to showcase the designs. once the design is chosen we will provide the actual details.
Updates

Dear All,

We wouldlike to extend our apology for not being able to provide feedbacks to everysingle design. We were extremely busy and we have multiple contests opensimultaneously which makes the process harder. However, thank you all for theefforts you have put into this contest. We have received anoverwhelming quality responses & it has been a very difficult task tochoose just one, we easily Loved at least several designs...

Thanksagain for participating, we wish you all success in your design ventures.

Kindregards,

HLW Team

Industry/Entity Type

It Company

```html
<!DOCTYPE html>
<html lang="en">
<head>
<meta charset="utf-8">
<title>Harbor Lantern – Email Signature</title>
<link href="https://fonts.googleapis.com/css2?family=Arimo:wght@400;700&display=swap" rel="stylesheet">
<style>
  :root {
    --bg: #ffffff;
    --ink-strong: #2b2b2b;
    --ink: #5a5a5a;
    --link: #1769c2;
    --brand: #1e88d8;
    --brand-accent: #7cc322;
    --divider: #c9c9c9;
    --icon: #8a949e;
  }
  * { margin: 0; padding: 0; box-sizing: border-box; }
  html, body {
    width: 1200px;
    height: 667px;
    overflow: hidden;
    background: var(--bg);
  }
  .signature {
    position: relative;
    width: 1200px;
    height: 667px;
    font-family: "Arimo", Arial, sans-serif;
  }
  .brand-mark {
    position: absolute;
    left: 184px;
    top: 298px;
    width: 405px;
    height: 70px;
    display: flex;
    align-items: center;
    justify-content: center;
    gap: 14px;
  }
  .brand-mark__dot {
    width: 22px;
    height: 22px;
    border-radius: 50%;
    background: var(--brand-accent);
    flex: none;
  }
  .brand-mark__name {
    font-size: 44px;
    font-weight: 700;
    color: var(--brand);
    letter-spacing: -0.5px;
    white-space: nowrap;
  }
  .divider {
    position: absolute;
    left: 615px;
    top: 211px;
    width: 2px;
    height: 245px;
    background: linear-gradient(to bottom, rgba(201,201,201,0), var(--divider) 20%, var(--divider) 80%, rgba(201,201,201,0));
  }
  .contact {
    position: absolute;
    left: 656px;
    top: 208px;
  }
  .contact__name {
    font-size: 28px;
    font-weight: 700;
    color: var(--ink-strong);
    line-height: 36px;
    margin-bottom: 6px;
  }
  .contact__line {
    font-size: 18px;
    color: var(--ink);
    line-height: 34.7px;
    white-space: nowrap;
  }
  .contact__link {
    color: var(--link);
    text-decoration: none;
  }
  .social {
    position: absolute;
    left: 657px;
    top: 403px;
    display: flex;
    gap: 13px;
    list-style: none;
  }
  .social__item {
    width: 43px;
    height: 43px;
    border-radius: 6px;
    background: var(--icon);
  }
</style>
</head>
<body>
  <main class="signature">
    <div class="brand-mark">
      <span class="brand-mark__name">Harbor Lantern</span>
      <span class="brand-mark__dot"></span>
    </div>

    <div class="divider"></div>

    <section class="contact">
      <h1 class="contact__name">Dana Whitfield</h1>
      <p class="contact__line">Tel: +555.014.2290</p>
      <p class="contact__line">Fax: +555.014.2291</p>
      <p class="contact__line">Email: <a class="contact__link" href="mailto:dana@harborlantern.com">dana@harborlantern.com</a></p>
      <p class="contact__line"><a class="contact__link" href="http://www.harborlantern.com">http://www.harborlantern.com</a></p>
    </section>

    <ul class="social" aria-label="Social profiles">
      <li class="social__item" role="img" aria-label="Social profile link"></li>
      <li class="social__item" role="img" aria-label="Social profile link"></li>
      <li class="social__item" role="img" aria-label="Social profile link"></li>
      <li class="social__item" role="img" aria-label="Social profile link"></li>
      <li class="social__item" role="img" aria-label="Social profile link"></li>
      <li class="social__item" role="img" aria-label="Social profile link"></li>
    </ul>
  </main>
</body>
</html>
```